The Nine Gates for Tablet Reliance - Contemporary Book Cover Design

The Nine Gates for Tablet Reliance was published in March 2019 and is available on Brimora and other platforms now. However, I am not happy with the cover.  It's a good design in some ways - I thought it would stand out and be easily recognizable. But I don't really like the color scheme and feel that a self-help book should probably use some lighter colors and that the red is too strident. The color scheme carries over into other marketing materials like the website, social media, etc. and I don't like the red and black scheme for these purposes.
It's not essential that the cover contain an endorsement like the current one but it could. Here are some endorsements:
“A must-read for anyone who is addicted to or thinks they may have a problem with digital technology. This eloquent work will also be useful to academics and clinicians exploring potential solutions. The author recognizes the similarities between smartphone addiction and other addictions, and logically applies one of the most effective known solutions for addiction - The Nine Gates.”
-- Dale Wickersham: Noted Interventionist, Keynote Speaker and Addiction Visionary
“If you suffer from digital addiction, I strongly encourage you to use this book as your road map to get you back to the real world.”
-- Thomas Quillard, Founder of Online Channel Monitor.
The back cover would have the new design / color scheme, but can have similar text, bio, author image, etc. Or we could include the endorsements there and shorten the other text.
As for the cover it could be stylized, or an image, a partial image, or whatever. I am open to suggestions. Think about what would be inviting for a person searching for help with moderating their smartphone use.
Let's add a subtitle as well "An Inner Journey to Balanced Tablet Habits"
Here is a link to the book:
https://www.brimora.example/Nine-Gates-Tablet-Reliance/dp/4086213590

Target Market(s)
General, since this issue affects almost everyone.
Colors
Designer to choose colors to be used in the design.
Look and feel

```html
<!DOCTYPE html>
<html lang="en">
<head>
<meta charset="utf-8">
<title>The Nine Gates for Tablet Reliance — Cover</title>
<link rel="stylesheet" href="https://fonts.googleapis.com/css2?family=Jost:wght@400;500;600;700&display=swap">
<style>
  :root {
    --stage: #2c3b3c;
    --paper: #f1f1f1;
    --endorse-red: #d6343b;
    --ink: #2a2a2a;
    --cyan: #1fa3cf;
    --navy: #1f5a99;
    --coral: #d2644f;
    --rule: #333333;
    --photo-light: #e9e9e7;
    --photo-mid: #b9b6b0;
    --photo-dark: #4a3f35;
    --white: #ffffff;
  }
  * { box-sizing: border-box; margin: 0; padding: 0; }
  html, body {
    width: 1200px;
    height: 969px;
    overflow: hidden;
    background: var(--stage);
  }
  .canvas {
    position: relative;
    width: 1200px;
    height: 969px;
    display: flex;
    align-items: center;
    justify-content: center;
  }
  .cover {
    position: relative;
    width: 640px;
    height: 910px;
    background: var(--paper);
    overflow: hidden;
    font-family: "Jost", "Futura", sans-serif;
    text-align: center;
  }
  .cover-photo {
    position: absolute;
    left: 0;
    right: 0;
    bottom: 0;
    height: 340px;
    z-index: 1;
    background:
      radial-gradient(ellipse 140px 200px at 52% 58%, var(--photo-dark) 0%, rgba(74,63,53,0.85) 55%, rgba(74,63,53,0) 100%),
      linear-gradient(180deg, var(--paper) 0%, var(--photo-light) 35%, var(--photo-mid) 75%, #6e665d 100%);
  }
  .endorsement,
  .title,
  .subtitle,
  .rule,
  .author { position: absolute; z-index: 2; }
  .endorsement {
    top: 32px;
    left: 40px;
    right: 32px;
    font-size: 17px;
    line-height: 22px;
    font-weight: 500;
    color: var(--endorse-red);
    text-transform: uppercase;
  }
  .endorsement .source {
    text-transform: none;
    color: var(--ink);
    font-weight: 400;
  }
  .title {
    top: 0;
    left: 0;
    right: 0;
    height: 0;
    font-weight: 700;
    line-height: 1;
    letter-spacing: -1px;
  }
  .title span {
    position: absolute;
    left: 0;
    right: 0;
    display: block;
  }
  .title .line-the { top: 104px; font-size: 70px; color: var(--cyan); }
  .title .line-gates { top: 176px; font-size: 76px; color: var(--cyan); }
  .title .line-for { top: 268px; font-size: 64px; color: var(--navy); }
  .title .line-tablet { top: 334px; font-size: 74px; color: var(--navy); }
  .title .line-reliance { top: 414px; font-size: 70px; color: var(--coral); }
  .rule {
    height: 2px;
    background: var(--rule);
  }
  .rule-top { top: 494px; left: 100px; width: 440px; }
  .subtitle {
    top: 500px;
    left: 100px;
    width: 440px;
    font-size: 23px;
    line-height: 29px;
    font-weight: 600;
    color: var(--ink);
    text-transform: uppercase;
  }
  .rule-bottom { top: 564px; left: 200px; width: 240px; }
  .author {
    left: 0;
    right: 0;
    bottom: 46px;
    font-size: 36px;
    line-height: 1;
    font-weight: 500;
    letter-spacing: 11px;
    color: var(--white);
    text-transform: uppercase;
  }
</style>
</head>
<body>
  <main class="canvas">
    <article class="cover">
      <div class="cover-photo" role="img" aria-label="Photo of a hooded figure holding a phone in front of their face against a pale blurred backdrop"></div>

      <p class="endorsement">If you suffer from digital addiction, I strongly encourage you to use this book as your road map to get you back to the real world. <span class="source">-Thomas Quillard, Founder of Online Channel Monitor.</span></p>

      <h1 class="title">
        <span class="line-the">THE</span>
        <span class="line-gates">NINE GATES</span>
        <span class="line-for">FOR</span>
        <span class="line-tablet">TABLET</span>
        <span class="line-reliance">RELIANCE</span>
      </h1>

      <div class="rule rule-top"></div>
      <p class="subtitle">An Inner Journey to Balanced<br>Tablet Habits</p>
      <div class="rule rule-bottom"></div>

      <p class="author">Jonah Reddel</p>
    </article>
  </main>
</body>
</html>
```